Quillmont Renovations Letterhead

Quillmont does not do actual renovation, but rather handles high end project management of renovation (primarily residential with an eye toward commercial and International) The renovation work could look very different between projects. This company works directly with the clients and manages the work of contractors, architects and interior designers (either subcontracted directly by Quillmont or hired by the client and entrusted to Quillmont to manage). Clients are high end in the economic scale and all materials should speak to that audience. Provoke a sense of change, openness and imagination, trust and integrity. The owner is female, but the audience will be heavily slanted male. It should not be a "feminine" or "masculine" looking . If anything, slant more on the masculine side.

Clean, simple, yet creative and artistically appealing. The logo should be clear and not competing with too many surrounding design elements.

There is a contest also on for business card. Please check that section if you would like to compete for both.

Get your creative juices going!

Target Market(s)

High end cients. Additional audience: professionals (architects, etc...) designers, contractors

Industry/Entity Type

Residential

Requirements
Must have
• Logo must be included in all materials

```html
<!DOCTYPE html>
<html lang="en">
<head>
<meta charset="utf-8">
<title>Quillmont Renovations Stationery</title>
<link href="https://fonts.googleapis.com/css2?family=Jost:wght@400;500;600&display=swap" rel="stylesheet">
<style>
  :root {
    --teal: #1aa99b;
    --charcoal: #3c3c3e;
    --paper: #ffffff;
    --backdrop: #e8e4de;
    --rule: #c9c9c9;
    --text: #4a4a4a;
  }
  * { margin: 0; padding: 0; box-sizing: border-box; }
  html, body {
    width: 1200px; height: 1177px; overflow: hidden;
    background: var(--backdrop);
    font-family: "Jost", Arial, sans-serif;
  }
  .canvas { position: relative; width: 1200px; height: 1177px; }

  .letterhead {
    position: absolute; left: 58px; top: 38px;
    width: 841px; height: 1088px;
    background: var(--paper);
    box-shadow: 0 2px 6px rgba(0,0,0,.18);
    overflow: hidden;
  }
  .brand-name {
    position: absolute; display: flex; align-items: center; gap: 10px;
    color: var(--charcoal); font-weight: 600; letter-spacing: .3px;
    white-space: nowrap; line-height: 1;
  }
  .brand-mark { background: var(--teal); flex: none; }
  .letterhead .brand-name { left: 33px; top: 111px; font-size: 23px; }
  .letterhead .brand-mark { width: 13px; height: 13px; }

  .contact-list {
    position: absolute; list-style: none;
    border-left: 2px solid var(--rule);
    color: var(--text);
  }
  .contact-list li { display: flex; align-items: center; gap: 6px; white-space: nowrap; }
  .contact-list svg { flex: none; }
  .letterhead .contact-list {
    left: 590px; top: 56px; padding-left: 14px; font-size: 13px;
  }
  .letterhead .contact-list li { height: 30px; }

  .footer-wave { position: absolute; left: 0; bottom: 0; display: block; }
  .footer-address { fill: #fff; font-family: "Jost", Arial, sans-serif; letter-spacing: .6px; }

  .business-card {
    position: absolute; left: 640px; top: 427px;
    width: 520px; height: 297px;
    background: var(--paper);
    box-shadow: 0 2px 8px rgba(0,0,0,.25);
    overflow: hidden;
  }
  .business-card .brand-name { left: 32px; top: 144px; font-size: 14.5px; gap: 7px; letter-spacing: .2px; }
  .business-card .brand-mark { width: 9px; height: 9px; }
  .business-card .contact-list {
    left: 270px; top: 50px; padding-left: 14px; font-size: 12px;
  }
  .holder-name { color: var(--teal); font-weight: 500; letter-spacing: .5px; height: 19px; }
  .holder-title { color: var(--charcoal); height: 30px; align-items: flex-start !important; }
  .business-card .contact-list li.detail { height: 30px; }
</style>
</head>
<body>
<main class="canvas">

  <section class="letterhead" aria-label="Letterhead">
    <div class="brand-name"><span class="brand-mark"></span>QUILLMONT RENOVATIONS</div>

    <ul class="contact-list">
      <li>
        <svg width="10" height="12" viewBox="0 0 10 12"><path d="M3 1 L1.5 2 C0 5 2 10 6 11.5 L8 10.5 L6.5 8 L5 8.6 C3.8 7.5 3 5.8 3.2 4.2 L4.5 3.6 Z" fill="var(--teal)"/></svg>
        123-456-7890
      </li>
      <li>
        <svg width="11" height="9" viewBox="0 0 11 9"><rect x=".5" y="1" width="10" height="7.5" fill="var(--teal)"/><path d="M.5 1 L5.5 5 L10.5 1" stroke="#fff" fill="none"/></svg>
        info@quillmontrenovations.com
      </li>
      <li>
        <svg width="11" height="11" viewBox="0 0 11 11"><circle cx="5.5" cy="5.5" r="5" fill="var(--teal)"/><path d="M.5 5.5 H10.5 M5.5 .5 C3 3 3 8 5.5 10.5 M5.5 .5 C8 3 8 8 5.5 10.5" stroke="#fff" stroke-width=".8" fill="none"/></svg>
        www.quillmontrenovations.com
      </li>
    </ul>

    <svg class="footer-wave" width="841" height="162" viewBox="0 0 841 162">
      <path d="M0 8 C170 78 420 100 841 12 L841 162 L0 162 Z" fill="var(--teal)"/>
      <path d="M0 0 C170 60 420 84 800 6 C420 76 170 64 0 2 Z" fill="var(--charcoal)"/>
      <text class="footer-address" x="420" y="125" text-anchor="middle" font-size="14">00, complex name, street, city 00000</text>
    </svg>
  </section>

  <section class="business-card" aria-label="Business card">
    <div class="brand-name"><span class="brand-mark"></span>QUILLMONT RENOVATIONS</div>

    <ul class="contact-list">
      <li class="holder-name">YOUR NAME</li>
      <li class="holder-title">TITLE</li>
      <li class="detail">
        <svg width="9" height="11" viewBox="0 0 10 12"><path d="M3 1 L1.5 2 C0 5 2 10 6 11.5 L8 10.5 L6.5 8 L5 8.6 C3.8 7.5 3 5.8 3.2 4.2 L4.5 3.6 Z" fill="var(--teal)"/></svg>
        123-456-7890
      </li>
      <li class="detail">
        <svg width="10" height="8" viewBox="0 0 11 9"><rect x=".5" y="1" width="10" height="7.5" fill="var(--teal)"/><path d="M.5 1 L5.5 5 L10.5 1" stroke="#fff" fill="none"/></svg>
        info@quillmontrenovations.com
      </li>
      <li class="detail">
        <svg width="10" height="10" viewBox="0 0 11 11"><circle cx="5.5" cy="5.5" r="5" fill="var(--teal)"/><path d="M.5 5.5 H10.5 M5.5 .5 C3 3 3 8 5.5 10.5 M5.5 .5 C8 3 8 8 5.5 10.5" stroke="#fff" stroke-width=".8" fill="none"/></svg>
        www.quillmontrenovations.com
      </li>
    </ul>

    <svg class="footer-wave" width="520" height="86" viewBox="0 0 520 86">
      <path d="M0 6 C120 42 280 46 520 10 L520 86 L0 86 Z" fill="var(--teal)"/>
      <path d="M36 0 C130 32 290 32 496 2 C290 38 130 40 36 1 Z" fill="var(--charcoal)"/>
      <text class="footer-address" x="260" y="61" text-anchor="middle" font-size="12.5">00, complex name, street, city 00000</text>
    </svg>
  </section>

</main>
</body>
</html>
```